Need design for an App.

The app in question is related to security and crime events with real time feed, engagement with friends and posting pictures, we want a sleak, minimal style. There are 11 or 12 screens to be made. We are adding video file as suggestion. We are not sure about colors so we accept suggestions. We are also adding the logo.

Reason: Just giving more time to designers. Thanks.

Industry/Entity Type

Security

Font styles to use
Sans Serif

Requirements
Must have
• The app must have a Login view; a new user view (with nickname, email and pass); a retrieve pass view; a menu view with options for alert configuration, send emergency alert and send report, a feed view with the most popular reports (3 worldwide at the top and near reports after), a profile view with avatar and personal reports, a send emergency alert view with a camera view; a configuration view when the user can put up to 5 contacts to send the alert to them;a send report view with camera and options to configure the camera; a edit report view where the user can see the 3 photos he will update and add a comment of those photos.
Nice to have
• Check the files we are open minds
Should not have
• old design

```html
<!DOCTYPE html>
<html lang="en">
<head>
<meta charset="utf-8">
<title>Vigilo – App Screens</title>
<link href="https://fonts.googleapis.com/css2?family=Abel&family=Open+Sans:ital,wght@0,400;0,600;1,400&display=swap" rel="stylesheet">
<style>
  :root{
    --page:#ffffff;
    --screen:#0e0e10;
    --city-a:#2a2a2e;
    --city-b:#0b0b0d;
    --red:#c41e3a;
    --red-deep:#a8182f;
    --white:#ffffff;
    --ink:#1a1a1a;
    --muted:#bdbdbd;
    --field-text:#c41e3a;
  }
  *{box-sizing:border-box;margin:0;padding:0}
  html,body{width:1200px;height:619px;overflow:hidden;background:var(--page)}
  body{position:relative;font-family:"Abel",sans-serif}

  .screen{position:absolute;background:var(--screen);border-radius:6px;overflow:hidden;color:var(--white)}
  .screen--splash{left:20px;top:78px;width:261px;height:466px}
  .screen--login{left:341px;top:108px;width:224px;height:398px}
  .screen--register{left:635px;top:78px;width:257px;height:466px}
  .screen--contacts{left:953px;top:108px;width:223px;height:398px}

  .backdrop{position:absolute;inset:0;background:radial-gradient(ellipse at 50% 30%,var(--city-a),var(--city-b) 75%)}

  .status-bar{position:absolute;left:0;right:0;top:0;height:18px;display:flex;align-items:center;justify-content:space-between;padding:0 8px;font-family:"Open Sans",sans-serif;font-size:8px;color:var(--white);z-index:2}
  .status-bar__carrier::before{content:"●●●●○ ";letter-spacing:-1px;font-size:6px}
  .status-bar__battery{display:flex;align-items:center;gap:3px}
  .status-bar__battery i{display:inline-block;width:14px;height:7px;border:1px solid var(--white);border-radius:1px;background:linear-gradient(90deg,var(--white) 82%,transparent 82%)}

  .brand-card{position:absolute;background:var(--white);border-radius:8px;display:flex;flex-direction:column;align-items:center;justify-content:center;gap:10%}
  .brand-card__mark{background:var(--red);border-radius:12%}
  .brand-card__name{color:var(--ink);font-family:"Abel",sans-serif;line-height:1}

  .pager{position:absolute;left:0;right:0;display:flex;justify-content:center;gap:3px}
  .pager span{width:3px;height:3px;border-radius:50%;background:var(--white)}
  .pager span:first-child{background:var(--red)}

  .heading{position:absolute;left:0;right:0;text-align:center;letter-spacing:.5px;color:var(--white)}

  .field{position:absolute;background:var(--white);border-radius:10px;box-shadow:inset 0 0 0 2px var(--ink),0 0 0 1px var(--white);color:var(--field-text);display:flex;align-items:center;justify-content:center;letter-spacing:.5px}

  .button{position:absolute;background:var(--red);color:var(--white);border-radius:12px;display:flex;align-items:center;justify-content:center;letter-spacing:.6px}

  .copyright{position:absolute;left:0;right:0;text-align:center;font-family:"Open Sans",sans-serif;font-size:5.5px;color:var(--white);letter-spacing:.2px}
  .home-bar{position:absolute;left:50%;width:22px;height:3px;margin-left:-11px;border-radius:2px;background:#666}

  /* contacts screen */
  .alert-panel{position:absolute;left:0;right:0;top:18px;height:351px;background:var(--red);border-radius:0 0 14px 14px}
  .alert-panel__rule{position:absolute;left:0;right:0;height:1px;background:rgba(255,255,255,.7)}
  .alert-panel__lede{position:absolute;left:30px;right:30px;top:100px;text-align:center;font-family:"Open Sans",sans-serif;font-style:italic;font-size:6px;line-height:1.3}
  .alert-panel__prompt{position:absolute;left:0;right:0;top:128px;text-align:center;font-family:"Open Sans",sans-serif;font-size:8.5px}
  .field--contact{border-radius:9px;box-shadow:inset 0 0 0 1.5px var(--red-deep),0 0 0 1px var(--white);font-family:"Open Sans",sans-serif;font-size:7.5px}
  .button--deep{background:var(--red-deep);font-family:"Open Sans",sans-serif}
</style>
</head>
<body>

<!-- Splash -->
<section class="screen screen--splash">
  <div class="backdrop" role="img" aria-label="Dark photograph of city towers seen from street level"></div>
  <div class="status-bar"><span class="status-bar__carrier">Nimbus</span><span class="status-bar__battery">82% <i></i></span></div>
  <div class="brand-card" style="left:68px;top:125px;width:119px;height:169px">
    <div class="brand-card__mark" style="width:74px;height:74px"></div>
    <div class="brand-card__name" style="font-size:34px">vigilo</div>
  </div>
  <div class="pager" style="top:316px"><span></span><span></span><span></span><span></span><span></span><span></span></div>
  <div class="copyright" style="top:436px">COPYRIGHT ©2014 VIGILO. ALL RIGHTS RESERVED</div>
  <div class="home-bar" style="top:452px"></div>
</section>

<!-- Login -->
<section class="screen screen--login">
  <div class="backdrop" role="img" aria-label="Dark photograph of city towers seen from street level"></div>
  <div class="status-bar"><span class="status-bar__carrier">Nimbus</span><span class="status-bar__battery">82% <i></i></span></div>
  <div class="brand-card" style="left:59px;top:24px;width:104px;height:146px">
    <div class="brand-card__mark" style="width:64px;height:64px"></div>
    <div class="brand-card__name" style="font-size:30px">vigilo</div>
  </div>
  <div class="pager" style="top:188px"><span></span><span></span><span></span><span></span><span></span><span></span></div>
  <div class="heading" style="top:203px;font-size:8px">LOGIN WITH YOUR CREDENTIALS</div>
  <div class="field" style="left:16px;top:226px;width:190px;height:23px;font-size:8.5px">User Name</div>
  <div class="field" style="left:16px;top:264px;width:190px;height:23px;font-size:8.5px">Password</div>
  <div class="button" style="left:16px;top:304px;width:77px;height:23px;font-size:10px">LOGIN</div>
  <div class="button" style="left:127px;top:304px;width:77px;height:23px;font-size:10px">FORGET?</div>
  <div class="button" style="left:40px;top:338px;width:143px;height:22px;font-size:10px">NOT A MEMBER? SIGN UP</div>
  <div class="copyright" style="top:377px;font-size:5px">COPYRIGHT ©2014 VIGILO. ALL RIGHTS RESERVED</div>
  <div class="home-bar" style="top:389px"></div>
</section>

<!-- Register -->
<section class="screen screen--register">
  <div class="backdrop" role="img" aria-label="Dark photograph of city towers seen from street level"></div>
  <div class="status-bar"><span class="status-bar__carrier">Nimbus</span><span class="status-bar__battery">82% <i></i></span></div>
  <div class="brand-card" style="left:88px;top:27px;width:82px;height:114px">
    <div class="brand-card__mark" style="width:50px;height:50px"></div>
    <div class="brand-card__name" style="font-size:24px">vigilo</div>
  </div>
  <div class="pager" style="top:156px"><span></span><span></span><span></span><span></span><span></span><span></span></div>
  <div class="heading" style="top:177px;font-size:9.5px">REGISTER WITH BELOW DETAILS</div>
  <div class="field" style="left:20px;top:208px;width:218px;height:27px;font-size:10px">User Name</div>
  <div class="field" style="left:20px;top:252px;width:218px;height:27px;font-size:10px">Nick Name</div>
  <div class="field" style="left:20px;top:295px;width:218px;height:27px;font-size:10px">Email</div>
  <div class="field" style="left:20px;top:338px;width:218px;height:27px;font-size:10px">Password</div>
  <div class="button" style="left:47px;top:387px;width:163px;height:24px;font-size:12px">REGISTER</div>
  <div class="copyright" style="top:436px">COPYRIGHT ©2014 VIGILO. ALL RIGHTS RESERVED</div>
  <div class="home-bar" style="top:452px"></div>
</section>

<!-- Alert contacts -->
<section class="screen screen--contacts">
  <div class="status-bar"><span class="status-bar__carrier">Nimbus</span><span class="status-bar__battery">82% <i></i></span></div>
  <div class="alert-panel">
    <svg class="alert-panel__menu" width="16" height="12" viewBox="0 0 16 12" style="position:absolute;left:6px;top:8px">
      <rect y="0" width="16" height="2.2" fill="#fff"/><rect y="5" width="16" height="2.2" fill="#fff"/><rect y="10" width="16" height="2.2" fill="#fff"/>
    </svg>
    <svg class="alert-panel__signal" width="18" height="14" viewBox="0 0 18 14" style="position:absolute;right:8px;top:6px" fill="none" stroke="#fff" stroke-width="1.4">
      <circle cx="14" cy="11" r="1.4" fill="#fff" stroke="none"/>
      <path d="M10 11a4 4 0 0 1 4-4"/><path d="M7 11a7 7 0 0 1 7-7"/>
      <path d="M1 5a6 6 0 0 1 8 0"/><path d="M3 7.5a3 3 0 0 1 4 0"/>
    </svg>
    <div class="alert-panel__rule" style="top:26px"></div>
    <svg class="alert-panel__avatar" width="52" height="52" viewBox="0 0 52 52" style="position:absolute;left:86px;top:39px">
      <circle cx="26" cy="26" r="24" fill="none" stroke="#fff" stroke-width="3"/>
      <circle cx="26" cy="20" r="8" fill="#fff"/>
      <path d="M12 42c2-9 8-12 14-12s12 3 14 12z" fill="#fff"/>
    </svg>
    <p class="alert-panel__lede">Lorem Ipsum is simply dummy text of the printing and typesetting industry.</p>
    <div class="alert-panel__rule" style="top:118px"></div>
    <p class="alert-panel__prompt">Mention upto 5 contacts to send alert</p>
    <div class="field field--contact" style="left:17px;top:152px;width:188px;height:22px">Phone Number 1</div>
    <div class="field field--contact" style="left:17px;top:181px;width:188px;height:22px">Phone Number 2</div>
    <div class="field field--contact" style="left:17px;top:210px;width:188px;height:22px">Phone Number 3</div>
    <div class="field field--contact" style="left:17px;top:239px;width:188px;height:22px">Phone Number 4</div>
    <div class="field field--contact" style="left:17px;top:268px;width:188px;height:22px">Phone Number 5</div>
    <div class="button button--deep" style="left:42px;top:309px;width:141px;height:22px;font-size:9px">REGISTER</div>
  </div>
  <div class="copyright" style="top:377px;font-size:5px">COPYRIGHT ©2014 VIGILO. ALL RIGHTS RESERVED</div>
  <div class="home-bar" style="top:389px"></div>
</section>

</body>
</html>
```